Crestline Slate & Tile Needs a Business Card

Attached you will find your logo, my photo and design guidelines for a new business card. The final design will need two separate files to create an embossed card. The cards will be printed by www.plinkprint.com (Instructions below)
Format is the Zib SQUARE card
Crestline Slate And Tile is a brick and mortar, retail stone and tile shop.
One the front:
Crestline Slate And Tile
Gerald Finchcombe
Owner
48207 Vesper Hollow Blvd
Suite R & T
Charlotte, NC 28953
Cell: 704-555-0183
Web: www.CrestlineSlateAndTile.com
(Make each word of the domain a different or alternating color)
On the back;
Something that shows beautiful colorful tile
Follow the design guide closely please. For more information see this page that describes creating the spot gloss file: https://www.plinkprint.com/us/business-cards/design-guidelines-spot-gloss
The logo is what we would like to have raised spot glossed.
Format is the Zib SQUARE card. See attahced guidlines.

```html
<!DOCTYPE html>
<html lang="en">
<head>
<meta charset="utf-8">
<title>Crestline Slate &amp; Tile – Square Business Card</title>
<link rel="stylesheet" href="https://fonts.googleapis.com/css2?family=Libre+Baskerville:wght@400;700&family=Lato:wght@400&display=swap">
<style>
  :root {
    --canvas: #ffffff;
    --card: #ffffff;
    --navy: #21323a;
    --navy-deep: #1a2a31;
    --steel: #6f8d9c;
    --steel-mid: #3f5966;
    --gold: #a8762f;
    --rust: #a8432b;
    --ink: #1f2a30;
    --white: #ffffff;
  }
  * { margin: 0; padding: 0; box-sizing: border-box; }
  html, body { width: 1200px; height: 1000px; overflow: hidden; background: var(--canvas); }
  .stage { position: relative; width: 1200px; height: 1000px; }

  .card {
    position: absolute; top: 266px; width: 469px; height: 469px;
    background: var(--card); overflow: hidden;
    box-shadow: 0 2px 6px rgba(0,0,0,0.18);
  }
  .card--front { left: 108px; }
  .card--back { left: 623px; }

  /* Front: brand */
  .brand { position: absolute; left: 48px; top: 42px; display: flex; align-items: center; gap: 30px; }
  .brand__mark { width: 80px; height: 80px; background: var(--gold); transform: rotate(45deg) scale(0.8); }
  .brand__name { font-family: "Libre Baskerville", serif; font-weight: 400; color: var(--navy); line-height: 1; }
  .brand__name .line1 { display: block; font-size: 33px; letter-spacing: 3px; }
  .brand__name .line2 { display: block; font-size: 15px; letter-spacing: 6px; margin-top: 14px; }
  .brand__name .amp { color: var(--rust); }

  /* Front: name band */
  .rule { position: absolute; left: 0; width: 100%; height: 3px; }
  .rule--gold { top: 179px; background: var(--gold); }
  .rule--rust { top: 274px; background: var(--rust); }
  .name-band { position: absolute; left: 0; top: 187px; width: 100%; height: 85px; background: var(--navy); color: var(--white); }
  .name-band__name { position: absolute; left: 40px; top: 13px; font-family: "Libre Baskerville", serif; font-weight: 700; font-size: 27px; letter-spacing: 0.5px; white-space: nowrap; }
  .name-band__title { position: absolute; left: 46px; top: 50px; font-family: "Lato", sans-serif; font-size: 16px; }

  /* Front: contact */
  .contact { position: absolute; left: 44px; top: 308px; list-style: none; font-family: "Lato", sans-serif; font-size: 16.5px; color: var(--ink); line-height: 22.5px; }
  .contact li { display: flex; gap: 10px; margin-bottom: 7px; }
  .contact svg { flex: none; width: 13px; height: 14px; margin-top: 4px; }
  .domain__word--alt { color: var(--gold); }

  .portrait {
    position: absolute; left: 277px; top: 294px; width: 192px; height: 175px;
    background: radial-gradient(ellipse at 50% 38%, #c99a80 0%, #a97a64 30%, #4a5260 62%, #2b3444 100%);
  }

  /* Back */
  .tile-field {
    position: absolute; inset: 0;
    background:
      radial-gradient(ellipse at 10% 50%, rgba(140,170,185,0.55) 0%, rgba(140,170,185,0) 60%),
      linear-gradient(90deg, var(--steel) 0%, var(--steel-mid) 28%, #2a3f48 55%, var(--navy-deep) 100%);
  }
  .back-brand { position: absolute; left: 195px; top: 358px; width: 178px; text-align: center; font-family: "Libre Baskerville", serif; font-weight: 400; color: var(--white); line-height: 1; }
  .back-brand .line1 { display: block; font-size: 25px; letter-spacing: 2px; }
  .back-brand .line2 { display: block; font-size: 11.5px; letter-spacing: 4.5px; margin-top: 12px; }
  .back-brand .amp { color: var(--gold); }
</style>
</head>
<body>
<main class="stage">
  <section class="card card--front" aria-label="Business card front">
    <div class="brand">
      <div class="brand__mark" aria-hidden="true"></div>
      <p class="brand__name"><span class="line1">CRESTLINE</span><span class="line2">SLATE &amp; TILE</span></p>
    </div>

    <div class="rule rule--gold"></div>
    <div class="name-band">
      <h1 class="name-band__name">GERALD FINCHCOMBE</h1>
      <p class="name-band__title">Owner</p>
    </div>
    <div class="rule rule--rust"></div>

    <ul class="contact">
      <li>
        <svg viewBox="0 0 13 14" aria-hidden="true"><path d="M6.5 0C3.6 0 1.5 2.1 1.5 4.9 1.5 8.4 6.5 14 6.5 14s5-5.6 5-9.1C11.5 2.1 9.4 0 6.5 0zm0 7a2 2 0 1 1 0-4 2 2 0 0 1 0 4z" fill="#a8762f"/></svg>
        <span>48207 Vesper Hollow Blvd<br>Suite R &amp; T<br>Charlotte, NC 28953</span>
      </li>
      <li>
        <svg viewBox="0 0 13 14" aria-hidden="true"><rect x="3" y="0.8" width="7" height="12.4" rx="1.3" fill="none" stroke="#a8762f" stroke-width="1.5"/><circle cx="6.5" cy="11" r="0.8" fill="#a8762f"/></svg>
        <span>704-555-0183</span>
      </li>
      <li>
        <svg viewBox="0 0 13 14" aria-hidden="true"><circle cx="6.5" cy="7" r="5.8" fill="#a8762f"/><path d="M3 5.5c1.5-.5 2 .8 3 .4s.6-2 2-2.3M5 12c0-2 1.5-2 2.5-3s2.5 0 3.5-1" fill="none" stroke="#fff" stroke-width="1"/></svg>
        <span class="domain"><span class="domain__word">Crestline</span><span class="domain__word domain__word--alt">Slate</span><span class="domain__word">And</span><span class="domain__word domain__word--alt">Tile</span><span class="domain__word">.com</span></span>
      </li>
    </ul>

    <div class="portrait" role="img" aria-label="Portrait photo of the owner, Gerald Finchcombe"></div>
  </section>

  <section class="card card--back" aria-label="Business card back">
    <div class="tile-field" role="img" aria-label="Embossed pattern of repeating decorative tiles in steel blue and dark slate"></div>
    <p class="back-brand"><span class="line1">CRESTLINE</span><span class="line2">SLATE &amp; TILE</span></p>
  </section>
</main>
</body>
</html>
```